Urine collection cup with and without sterile seal sticker

Hello. We need a urine cup label designed please with

Name:
Date of Birth:
Date:
Time:
Temp℃:
Specimen ID:

Product code: TUB-47
Volume markings (e.g., 30 mL, 60 mL, 90 mL).
Vela Drug Tests logo

Could you please provide one version with the additional sterile sticker extending to the top, and one version without the additional sterile sticker?

```html
<!DOCTYPE html>
<html lang="en">
<head>
<meta charset="utf-8">
<title>Vela Drug Tests – Specimen Container Labels</title>
<link href="https://fonts.googleapis.com/css2?family=Roboto:ital,wght@0,400;0,500;0,700;1,700&display=swap" rel="stylesheet">
<style>
  :root{
    --sky:#4DC3FC;
    --navy:#07338F;
    --ink:#0A3A8A;
    --panel:#E6E6E6;
    --white:#FFFFFF;
    --hazard:#F5C518;
    --vol-30:#F9B800;
    --vol-60m:#F012BE;
    --vol-60g:#5CEB0B;
  }
  html,body{margin:0;padding:0;overflow:hidden;background:var(--white);}
  .sheet{display:block;width:1200px;height:780px;font-family:'Roboto',Arial,sans-serif;}
  .frame-sky{fill:var(--sky);}
  .frame-navy{fill:var(--navy);}
  .panel{fill:var(--panel);}
  .field{fill:var(--ink);font-size:22.5px;font-weight:400;}
  .rule{stroke:var(--ink);stroke-width:1.6;}
  .brand{fill:var(--ink);font-size:20px;font-weight:700;}
  .hazard{fill:var(--hazard);}
  .code{fill:var(--white);font-size:13px;font-weight:700;}
  .side-note{fill:var(--ink);font-size:12.5px;font-weight:700;font-style:italic;}
  .side-title{fill:var(--white);font-size:23px;font-weight:700;}
  .tab-title{fill:var(--navy);font-size:46px;font-weight:700;}
  .vol-num{font-size:28px;font-weight:700;}
  .vol-unit{font-size:14px;font-weight:700;}
  .vol-dark{fill:var(--ink);}
  .vol-light{fill:var(--white);}
  .caption{fill:var(--ink);font-size:22px;font-weight:400;}
</style>
</head>
<body>
<svg class="sheet" viewBox="-15 0 2400 1560" width="1200" height="780" xmlns="http://www.w3.org/2000/svg">
  <defs>
    <clipPath id="label-shape">
      <rect x="0" y="0" width="498" height="300" rx="40"/>
    </clipPath>

    <g id="sterile-tab">
      <path class="frame-sky" d="M399 0 V-220 A49.5 49.5 0 0 1 498 -220 V0 Z"/>
      <text class="tab-title" transform="translate(432 -215) rotate(90)" textLength="160" lengthAdjust="spacingAndGlyphs">STERILE</text>
    </g>

    <g id="specimen-label">
      <rect class="frame-sky" x="0" y="0" width="498" height="300" rx="40"/>
      <rect class="frame-navy" x="339" y="0" width="159" height="300" rx="40"/>
      <rect class="frame-sky" x="339" y="0" width="60" height="300"/>
      <rect class="frame-sky" x="23" y="25" width="426" height="250" rx="30"/>
      <path class="panel" d="M53 25 H399 V275 H53 A30 30 0 0 1 23 245 V55 A30 30 0 0 1 53 25 Z"/>

      <text class="field" x="50" y="67">Date:</text>
      <line class="rule" x1="110" y1="70" x2="208" y2="70"/>
      <text class="field" x="238" y="67">Time:</text>
      <line class="rule" x1="300" y1="70" x2="399" y2="70"/>

      <text class="field" x="50" y="110">Name</text>
      <text class="field" x="165" y="110">:</text>
      <line class="rule" x1="187" y1="113" x2="399" y2="113"/>

      <text class="field" x="50" y="153">Date of Birth:</text>
      <line class="rule" x1="187" y1="156" x2="399" y2="156"/>

      <text class="field" x="50" y="196">Specimen ID:</text>
      <line class="rule" x1="187" y1="199" x2="399" y2="199"/>

      <text class="field" x="50" y="239">Temp C:</text>
      <line class="rule" x1="138" y1="242" x2="210" y2="242"/>

      <text class="brand" x="236" y="246">Vela Drug Tests</text>

      <circle class="hazard" cx="424" cy="247" r="14"/>

      <text class="side-note" transform="translate(427 50) rotate(90)" textLength="130" lengthAdjust="spacingAndGlyphs">STERILE SINGLE USE</text>
      <text class="side-note" transform="translate(411 50) rotate(90)" textLength="172" lengthAdjust="spacingAndGlyphs">URINE SAMPLE CONTAINER</text>

      <text class="side-title" transform="translate(467 27) rotate(90)" textLength="246" lengthAdjust="spacingAndGlyphs">SPECIMEN CONTAINER</text>

      <text class="code" x="335" y="293">TUB-47</text>
    </g>
  </defs>

  <g transform="translate(115 387)">
    <use href="#sterile-tab"/>
    <use href="#specimen-label"/>
    <g clip-path="url(#label-shape)">
      <circle fill="var(--vol-30)" cx="88" cy="290" r="38"/>
      <text class="vol-dark" x="65" y="291"><tspan class="vol-num">30</tspan><tspan class="vol-unit">ml</tspan></text>
    </g>
  </g>
  <g transform="translate(653 387)">
    <use href="#specimen-label"/>
    <g clip-path="url(#label-shape)">
      <circle fill="var(--vol-30)" cx="88" cy="290" r="38"/>
      <text class="vol-dark" x="65" y="291"><tspan class="vol-num">30</tspan><tspan class="vol-unit">ml</tspan></text>
    </g>
  </g>
  <text class="caption" x="221" y="741">With  sterile sticker</text>

  <g transform="translate(1233 387)">
    <use href="#sterile-tab"/>
    <use href="#specimen-label"/>
    <g clip-path="url(#label-shape)">
      <circle fill="var(--vol-60m)" cx="88" cy="290" r="38"/>
      <text class="vol-light" x="65" y="291"><tspan class="vol-num">60</tspan><tspan class="vol-unit">ml</tspan></text>
    </g>
  </g>
  <g transform="translate(1771 387)">
    <use href="#specimen-label"/>
    <g clip-path="url(#label-shape)">
      <circle fill="var(--vol-60m)" cx="88" cy="290" r="38"/>
      <text class="vol-light" x="65" y="291"><tspan class="vol-num">60</tspan><tspan class="vol-unit">ml</tspan></text>
    </g>
  </g>
  <text class="caption" x="1334" y="741">With  sterile sticker</text>

  <g transform="translate(115 1101)">
    <use href="#sterile-tab"/>
    <use href="#specimen-label"/>
    <g clip-path="url(#label-shape)">
      <circle fill="var(--vol-60g)" cx="88" cy="290" r="38"/>
      <text class="vol-dark" x="65" y="291"><tspan class="vol-num">60</tspan><tspan class="vol-unit">ml</tspan></text>
    </g>
  </g>
  <g transform="translate(653 1101)">
    <use href="#specimen-label"/>
    <g clip-path="url(#label-shape)">
      <circle fill="var(--vol-60g)" cx="88" cy="290" r="38"/>
      <text class="vol-dark" x="65" y="291"><tspan class="vol-num">60</tspan><tspan class="vol-unit">ml</tspan></text>
    </g>
  </g>
  <text class="caption" x="221" y="1455">With  sterile sticker</text>
</svg>
</body>
</html>
```